Professional Hairdresser needs powerful, clever, simple, modern business card

I need a professional, clever, powerful, bold, attractive, modern/simplistic business card.
I specialize in dimensional hair color, precision haircutting, modern classic design, and signature finishes.
I believe in advanced education, continued training with emphasis on perfect practice, and strive to be the best at what I do.
I am trained by the industry's best and have passion for what I do, I want my business card to reflect my talents, education, capabilities, signature color techniques and design and confidence.
I want to be known as reputable, bold, artistic, aware, classic yet modern, innovative, creative, dimensional, knowledgeable, and educated.
I want something bold, simple, elegant, modern, clever, and legible.
My personal style is progressive, modern, eclectic, clean with modern luxury comfort style.
I love the use of black and white, to creative visual interest and texture. I think putting black as a solid background with white bold font makes the words jump/glow to the eye. I also think a stark white background with bold black fonts looks great, maybe with a punch of red. It is simple, clean, elegant.
I have a QR code I would like to include on the card but have no idea how to make it visually pleasing or make sense.
I do not have a set logo and am not sure if this needs to be done first or if the business card should be done first.

Target Market(s)

Early 20's-mid 60's, female and male, fashion aware, people who can afford my prices, appreciate value

Industry/Entity Type

Training

Requirements
Must have
• I would like to incorporate the QR code I have if possible.
I would like to have my name and contact info.
I would like my logo (or maybe have my logo be RT in a font like listed below).
I would like the fonts to be modern, bold, clean, readable.
Fonts I have looked at are: The font used on the book called: Vexaro A Hundred Years of Hue" I really love. I have looked at glyphvault.example for font and found "Georgiquas", but the designer wanted 200 euros which I just dont have at the time. Others I looked at include "Lin Libertine", Alien-Encounters-solid-regular-italic".
I love font used in the picture I included with the Tobin.Ashcroft ad.
Clean, modern, professional, legible, structured.
Nice to have
• I envision a black background with bold, modern, simple, font in white creating the effect of the words jumping off the card, visually apparent and glowing. Like a really expensive restaurant with a sign that you cant miss because the name is in bright white on black background, simple, bold, modern but not futuristic, powerful, clever, elegant, and draws the eye making it unforgetable. Perhaps layering black and white in order to where the font will be in white.
I see balance and chic.
Perhaps
Should not have
• I appreciate the trends in business design, but realize trends come and go and not sure if having something "trendy" is advisable for me. Having said that, I like creative modern design and sometimes current trends are important in design. I do like red as accent color, the primary blue color, blue on the PixelForum page, the masculine/florescent purple, and the neo bold yellow and the primary color shade of yellow.
I do not want clutter.
I do not want any fonts that are swirly, old-world calligraphy, script, or penmanship style.
I do not want picture of scissors, heads of old-school beauty school hair, or barber poles.

```html
<!DOCTYPE html>
<html lang="en">
<head>
<meta charset="utf-8">
<title>Rowan Tate — Business Card</title>
<link rel="stylesheet" href="https://fonts.googleapis.com/css2?family=Michroma&family=Roboto:wght@300&display=swap">
<style>
  :root {
    --ink-deep: #0d0f14;
    --ink-mid: #1b1f27;
    --haze-grey: rgba(150, 156, 168, 0.55);
    --haze-blue: rgba(30, 60, 150, 0.55);
    --haze-teal: rgba(30, 90, 80, 0.35);
    --name-white: #ffffff;
    --contact-grey: #b9bfca;
    --social-tint: #4f6a8c;
  }
  html, body {
    margin: 0;
    padding: 0;
    width: 1200px;
    height: 685px;
    overflow: hidden;
    background: var(--ink-deep);
  }
  .business-card {
    position: relative;
    width: 1200px;
    height: 685px;
    overflow: hidden;
    background:
      repeating-linear-gradient(90deg, rgba(255,255,255,0.018) 0 1px, transparent 1px 4px),
      radial-gradient(ellipse 380px 300px at 330px 310px, var(--haze-grey), transparent 70%),
      radial-gradient(ellipse 300px 260px at 820px 140px, rgba(120,126,140,0.28), transparent 70%),
      radial-gradient(ellipse 520px 240px at 300px 0px, var(--haze-blue), transparent 70%),
      radial-gradient(ellipse 300px 200px at 560px 0px, var(--haze-teal), transparent 70%),
      radial-gradient(ellipse 500px 260px at 200px 685px, rgba(40,70,130,0.35), transparent 70%),
      linear-gradient(90deg, var(--ink-mid) 0%, #20242c 40%, var(--ink-deep) 100%);
  }
  .card-name {
    position: absolute;
    left: 0;
    top: 0;
    width: 1200px;
    height: 685px;
  }
  .card-name text {
    font-family: "Michroma", sans-serif;
    font-size: 118px;
    fill: var(--name-white);
  }
  .contact-row {
    position: absolute;
    left: 43px;
    top: 630px;
    display: flex;
    align-items: center;
    font-family: "Roboto", sans-serif;
    font-weight: 300;
    color: var(--contact-grey);
    font-size: 27px;
    letter-spacing: 1.6px;
    white-space: nowrap;
  }
  .social-name {
    font-size: 14px;
    letter-spacing: 0.5px;
    color: var(--social-tint);
    margin-right: 8px;
  }
  .contact-phone { margin-left: 10px; }
  .contact-email { margin-left: 30px; }
  .contact-web { margin-left: 30px; }
</style>
</head>
<body>
  <main class="business-card">
    <svg class="card-name" viewBox="0 0 1200 685" aria-label="Rowan Tate">
      <text x="119" y="384" textLength="965" lengthAdjust="spacingAndGlyphs">ROWAN TATE</text>
    </svg>
    <div class="contact-row">
      <span class="social-name">Chirp</span>
      <span class="social-name">Folio</span>
      <span class="contact-phone">555 014 2738</span>
      <span class="contact-email">rowan@rowantatepro.com</span>
      <span class="contact-web">www.rowantatepro.com</span>
    </div>
  </main>
</body>
</html>
```